Norvale Works - pioneers of next generation consulting!

We are a next generation management consulting firm with two focus areas and USPs (unique selling points):>Technology driven business developmentWe are not developers, we are experts in HOW to apply and incorporate technology in your business dna to drive business growth and value-added change.>Creating high performing teams levering our philosophy of collective intelligence. We truly understand the need of human engagement and we know that the only way of getting there is by building strong relationships among people, a warm and open culture is a stepping stone towards effective collaboration within/among teams. - We don't want a ”corporate feel” to our templates. The organic feeling we have with our blue-on-blue blobs has the idea of ever changing movement and shape changing. Please see our website, www.norvaleworks.se. - In our context we sit among classic business mgmt. consultants and classic IT mgmt. consultants. We cater to business, tech and humans as the ultimate vehicle of change and business value. -To have a clean template one suggestion is to only use blue, white and black and keeping other colors separate, as an alternative but we are truly open allow your creativity add value to this. We are looking to find a slide deck which we can pick slides from, depending on what/whom/why we interact with customer we want to create different outcomes and our presentations should support this.

Industry/Entity Type

Management Consulting

Requirements
Must have
• next generation powerpoint and how to package storytelling. please keep to our look and feel, we just arrived at our logo, colours and shapes. Help us to carry it into our ppt's as well.
Should not have
• Hi all, please have a look at our website. It is still very new and more will be done, but our goal is to make powerpoint to come alive again and mirror our pioneering hearts and brains.

```html
<!DOCTYPE html>
<html lang="en">
<head>
<meta charset="utf-8">
<title>Norvale Works – Slide Template</title>
<link href="https://fonts.googleapis.com/css2?family=Raleway:wght@300;400;500;600;700;800&display=swap" rel="stylesheet">
<style>
  :root {
    --brand-blue: #1b52c4;
    --cover-blue: #2148aa;
    --outline-blue: #2c55a8;
    --wave-green: #2fa84f;
    --ink: #161616;
    --body-ink: #2e2e2e;
    --paper: #ffffff;
    --stage: #000000;
  }
  * { box-sizing: border-box; margin: 0; padding: 0; }
  html, body {
    width: 1200px; height: 2663px; overflow: hidden;
    background: var(--stage);
    font-family: "Raleway", sans-serif;
  }
  .deck { position: relative; width: 1200px; height: 2663px; }
  .slide {
    position: absolute; left: 39px; width: 1113px; height: 834px;
    overflow: hidden; background: var(--paper);
  }
  .slide--cover { top: 32px; }
  .slide--summary { top: 909px; height: 832px; }
  .slide--columns { top: 1782px; height: 838px; }

  /* Cover */
  .cover-photo {
    position: absolute; inset: 0;
    background: radial-gradient(ellipse at 50% 45%, #2a55b8 0%, var(--cover-blue) 55%, #1a3d98 100%);
  }
  .cover-content {
    position: absolute; left: 0; right: 0; top: 368px;
    text-align: center; color: var(--paper);
  }
  .cover-brand { font-size: 64px; font-weight: 600; letter-spacing: 1px; line-height: 1; }
  .cover-title { margin-top: 50px; font-size: 42px; font-weight: 700; line-height: 1; }
  .cover-subtitle { margin-top: 14px; font-size: 35px; font-weight: 400; line-height: 1; }

  /* Header */
  .slide-header { position: absolute; top: 18px; left: 0; right: 0; height: 50px; }
  .header-bar { position: absolute; left: 0; top: 0; width: 11px; height: 48px; background: var(--brand-blue); }
  .header-title {
    position: absolute; left: 21px; top: 6px;
    font-size: 37px; font-weight: 700; color: var(--ink); line-height: 1;
  }
  .header-brand {
    position: absolute; right: 22px; top: 14px;
    font-size: 34px; font-weight: 600; color: var(--brand-blue); line-height: 1; letter-spacing: 0.5px;
  }

  /* Summary slide */
  .summary { position: absolute; left: 36px; top: 168px; width: 450px; }
  .summary-heading { font-size: 37px; font-weight: 400; color: var(--ink); margin-bottom: 16px; letter-spacing: 0.5px; }
  .summary-text {
    font-size: 20.5px; line-height: 32px; color: var(--body-ink);
    letter-spacing: 0.4px; hyphens: auto; -webkit-hyphens: auto;
  }
  .summary-text + .summary-text { margin-top: 32px; }
  .summary-blob { position: absolute; left: 548px; top: 174px; width: 557px; height: 530px; }

  /* Columns slide */
  .column { position: absolute; top: 126px; width: 480px; text-align: center; }
  .column--left { left: 74px; }
  .column--right { left: 632px; }
  .column-blob { display: block; width: 412px; height: 366px; margin: 0 auto; }
  .column-title { margin-top: 40px; font-size: 31px; font-weight: 700; color: var(--brand-blue); line-height: 1.1; letter-spacing: 0.5px; }
  .column-text {
    width: 440px; margin: 12px auto 0;
    font-size: 20.5px; line-height: 32px; color: var(--body-ink); letter-spacing: 0.4px;
  }

  /* Footer */
  .slide-footer { position: absolute; left: 0; right: 0; bottom: 0; height: 80px; }
  .footer-wave { position: absolute; inset: 0; width: 100%; height: 100%; }
  .footer-copyright {
    position: absolute; left: 14px; bottom: 14px;
    font-size: 21px; color: var(--paper); font-weight: 400;
  }
  .footer-page {
    position: absolute; right: 18px; bottom: 10px;
    font-size: 21px; color: var(--paper); font-weight: 400;
  }
</style>
</head>
<body>
<main class="deck">

  <section class="slide slide--cover">
    <div class="cover-photo" role="img" aria-label="Team members using VR headsets in a bright office, tinted blue"></div>
    <div class="cover-content">
      <div class="cover-brand">NORVALE WORKS</div>
      <h1 class="cover-title">PROJECT TITLE HERE</h1>
      <p class="cover-subtitle">Subtext here</p>
    </div>
  </section>

  <section class="slide slide--summary">
    <header class="slide-header">
      <span class="header-bar"></span>
      <h2 class="header-title">PROJECT TITLE HERE</h2>
      <span class="header-brand">NORVALE WORKS</span>
    </header>

    <div class="summary">
      <h3 class="summary-heading">Summary</h3>
      <p class="summary-text">Customer expectations in the digital era is that we fully solve their need and not just a part of it. Added to that they expect a convenient and smooth experience and appreciate an unexpected tweak. You now you are the best to solve the basic cus&shy;tomer need but the effort to do it all is challenging. What you can do is to build the customer service ecosystem by using value network business models and ex&shy;celling in service &amp; offering structure.</p>
      <p class="summary-text">Customer expectations in the digital era is that we fully solve their need and not just a part of it. Added to that they expect a convenient and smooth experience</p>
    </div>

    <svg class="summary-blob" viewBox="0 0 600 570" role="img" aria-label="Colleagues reviewing a phone together at an office table">
      <defs>
        <linearGradient id="summaryPhotoTone" x1="0" y1="0" x2="1" y2="1">
          <stop offset="0" stop-color="#e4e6e5"/>
          <stop offset="0.5" stop-color="#b9b4aa"/>
          <stop offset="1" stop-color="#7e8284"/>
        </linearGradient>
      </defs>
      <path d="M300,8 C380,-4 500,4 560,50 C596,80 594,150 594,240 C594,330 590,410 560,450 C520,500 420,528 320,544 C220,560 100,566 50,520 C8,480 4,410 14,350 C26,270 90,200 150,140 C210,80 240,18 300,8 Z"
            fill="url(#summaryPhotoTone)" stroke="var(--outline-blue)" stroke-width="5"/>
    </svg>

    <footer class="slide-footer">
      <svg class="footer-wave" viewBox="0 0 1113 80" preserveAspectRatio="none" aria-hidden="true">
        <path d="M0,12 C280,-2 600,4 820,4 C960,4 1050,10 1113,18 L1113,80 L0,80 Z" fill="var(--wave-green)"/>
        <path d="M0,18 C280,6 600,10 820,10 C960,10 1050,16 1113,26 L1113,80 L0,80 Z" fill="var(--brand-blue)"/>
      </svg>
      <span class="footer-copyright">Copyright text here</span>
      <span class="footer-page">Page : 01</span>
    </footer>
  </section>

  <section class="slide slide--columns">
    <header class="slide-header">
      <span class="header-bar"></span>
      <h2 class="header-title">PROJECT TITLE HERE</h2>
      <span class="header-brand">NORVALE WORKS</span>
    </header>

    <article class="column column--left">
      <svg class="column-blob" viewBox="0 0 432 390" role="img" aria-label="Colleagues reviewing a phone together at an office table">
        <defs>
          <linearGradient id="teamPhotoTone" x1="0" y1="0" x2="1" y2="1">
            <stop offset="0" stop-color="#e2e4e3"/>
            <stop offset="0.5" stop-color="#b7b2a8"/>
            <stop offset="1" stop-color="#7c8082"/>
          </linearGradient>
        </defs>
        <path d="M210,8 C272,-8 334,36 372,108 C410,180 436,258 420,318 C404,368 330,382 220,382 C110,382 30,372 12,322 C-4,270 30,200 80,130 C120,72 160,22 210,8 Z"
              fill="url(#teamPhotoTone)" stroke="var(--outline-blue)" stroke-width="5"/>
      </svg>
      <h3 class="column-title">Paragraph Title here</h3>
      <p class="column-text">Lorem ipsum text here Lorem ipsum text here Lorem ipsum text here Lorem ipsum text here Lorem ipsum text here Lorem ipsum text here Lorem ipsum text here Lorem ipsum text here</p>
    </article>

    <article class="column column--right">
      <svg class="column-blob" viewBox="0 0 432 390" role="img" aria-label="Engineer working on an industrial robot arm in a workshop">
        <defs>
          <linearGradient id="workshopPhotoTone" x1="0" y1="0" x2="1" y2="1">
            <stop offset="0" stop-color="#eceeee"/>
            <stop offset="0.55" stop-color="#c0c4c8"/>
            <stop offset="1" stop-color="#848a92"/>
          </linearGradient>
        </defs>
        <path d="M226,10 C292,-6 366,30 400,104 C428,170 440,250 420,312 C402,366 320,384 214,384 C110,384 28,370 12,318 C-2,266 24,196 74,128 C118,68 170,24 226,10 Z"
              fill="url(#workshopPhotoTone)" stroke="var(--outline-blue)" stroke-width="5"/>
      </svg>
      <h3 class="column-title">Paragraph Title here</h3>
      <p class="column-text">Lorem ipsum text here Lorem ipsum text here Lorem ipsum text here Lorem ipsum text here Lorem ipsum text here Lorem ipsum text here Lorem ipsum text here Lorem ipsum text here</p>
    </article>

    <footer class="slide-footer">
      <svg class="footer-wave" viewBox="0 0 1113 80" preserveAspectRatio="none" aria-hidden="true">
        <path d="M0,12 C280,-2 600,4 820,4 C960,4 1050,10 1113,18 L1113,80 L0,80 Z" fill="var(--wave-green)"/>
        <path d="M0,18 C280,6 600,10 820,10 C960,10 1050,16 1113,26 L1113,80 L0,80 Z" fill="var(--brand-blue)"/>
      </svg>
      <span class="footer-copyright">Copyright text here</span>
      <span class="footer-page">Page : 01</span>
    </footer>
  </section>

</main>
</body>
</html>
```